I need creative and unique business card design using my company logo. Ok to change logo color. We are a small brokerage doing both Real Estate and Mortgage services. Need to have the follow on business card;
1. agent name - Mila Fenton - Realtor
2. cell - 949-555-0182
3. license number - DRE 04917362
4. business name - Brightway Estates & Lending, Inc
5. business office - 626-555-0147
6. business address - 287 W. Larkmoor Ave #214, Arcadia CA 91088
7. business logo - attached (ok to use different color on logo)

```html
<!DOCTYPE html>
<html lang="en">
<head>
<meta charset="utf-8">
<title>Mila Fenton — Business Card</title>
<link rel="stylesheet" href="https://fonts.googleapis.com/css2?family=Poppins:wght@400;500&family=Raleway:wght@700&display=swap">
<style>
  :root {
    --backdrop: #9b9b9b;
    --card-white: #ffffff;
    --brand-blue: #2a5db0;
    --brand-deep: #1f4a9a;
    --brand-sky: #4aa0dc;
    --back-blue: #2e67ae;
    --back-ink: #234f8f;
    --back-tile: #3f7fc6;
    --ink: #3c3c3c;
    --rule: #b8b8b8;
  }
  * { margin: 0; padding: 0; box-sizing: border-box; }
  html, body { width: 1093px; height: 1200px; overflow: hidden; }
  body {
    position: relative;
    background: var(--backdrop);
    font-family: "Poppins", sans-serif;
  }
  .card {
    position: absolute;
    left: 264px;
    width: 580px;
    height: 357px;
    overflow: hidden;
  }
  .card--front { top: 226px; background: var(--card-white); }
  .card--back { top: 620px; background: var(--back-blue); }

  .brand {
    position: absolute;
    text-align: center;
    font-family: "Poppins", sans-serif;
    font-weight: 500;
    letter-spacing: 0.28em;
    line-height: 1.35;
  }
  .brand__square { display: block; margin: 0 auto; }
  .brand__name { display: block; font-size: 13px; }

  .card--front .brand { left: 36px; top: 87px; width: 238px; color: var(--brand-blue); }
  .card--front .brand__square { width: 115px; height: 115px; background: var(--brand-blue); margin-bottom: 26px; }

  .divider {
    position: absolute;
    left: 289px; top: 74px;
    width: 1px; height: 209px;
    background: var(--rule);
  }
  .contact { position: absolute; left: 312px; top: 74px; color: var(--ink); }
  .contact__name {
    font-family: "Raleway", sans-serif;
    font-weight: 700;
    font-size: 22px;
    line-height: 26px;
    color: var(--brand-blue);
  }
  .contact__role { font-size: 16px; line-height: 18px; margin-bottom: 10px; }
  .contact__line {
    display: flex; align-items: center; gap: 3px;
    font-size: 16.5px; line-height: 27px;
  }
  .contact__line svg { width: 13px; height: 17px; fill: var(--brand-deep); }
  .contact__company { font-size: 16.5px; line-height: 22px; color: var(--brand-blue); margin-top: 6px; }
  .contact__address { font-size: 16.5px; line-height: 21px; }
  .contact__license { font-size: 16.5px; line-height: 22px; margin-top: 8px; }
  .contact__license b { font-weight: 500; color: var(--brand-deep); }

  .card__band {
    position: absolute; left: 0; bottom: 0;
    width: 100%; height: 9px;
    background: linear-gradient(90deg, var(--brand-deep) 0%, var(--brand-deep) 40%, var(--brand-sky) 58%, var(--brand-sky) 100%);
  }

  .card--back .brand { left: 0; top: 64px; width: 100%; color: var(--back-ink); }
  .card--back .brand__square {
    width: 146px; height: 146px;
    background: linear-gradient(225deg, var(--back-tile), var(--back-blue));
    margin-bottom: 28px;
  }
  .card--back .brand__name { font-size: 16px; letter-spacing: 0.3em; }
</style>
</head>
<body>
  <section class="card card--front">
    <div class="brand">
      <span class="brand__square"></span>
      <span class="brand__name">BRIGHTWAY</span>
      <span class="brand__name">ESTATES &amp; LENDING, INC</span>
    </div>
    <div class="divider"></div>
    <div class="contact">
      <h1 class="contact__name">MILA FENTON</h1>
      <p class="contact__role">Realtor</p>
      <p class="contact__line">
        <svg viewBox="0 0 12 18" aria-hidden="true"><path d="M2 0h8a2 2 0 0 1 2 2v14a2 2 0 0 1-2 2H2a2 2 0 0 1-2-2V2a2 2 0 0 1 2-2zm0 3v11h8V3zm4 12.2a.9.9 0 1 0 0 1.8.9.9 0 0 0 0-1.8z"/></svg>
        949-555-0182
      </p>
      <p class="contact__line">
        <svg viewBox="0 0 18 18" aria-hidden="true"><path d="M4 1l3 4-1.6 1.8a11 11 0 0 0 5.8 5.8L13 11l4 3-1.6 2.6C14.6 18 12 17.6 9 15.5A20 20 0 0 1 2.5 9C.4 6 0 3.4 1.4 2.6zM11 1a6 6 0 0 1 6 6h-1.5A4.5 4.5 0 0 0 11 2.5zm0 3a3 3 0 0 1 3 3h-1.5A1.5 1.5 0 0 0 11 5.5z"/></svg>
        626-555-0147
      </p>
      <p class="contact__company">Brightway Estates &amp; Lending, Inc</p>
      <p class="contact__address">287 W. Larkmoor Ave #214,<br>Arcadia CA 91088</p>
      <p class="contact__license"><b>LIC</b> DRE 04917362</p>
    </div>
    <div class="card__band"></div>
  </section>

  <section class="card card--back">
    <div class="brand">
      <span class="brand__square"></span>
      <span class="brand__name">BRIGHTWAY</span>
      <span class="brand__name">ESTATES &amp; LENDING, INC</span>
    </div>
  </section>
</body>
</html>
```